halbrook paving works

Needs to have phone number 0418352790 and email carlwhitby@mailnest.com.au.
ABN 27813046652
name carl whitby

For all your concreting solutions
Excavation
Exposed & colour concrete
House & shed slabs
Driveways
Landing & steps

Contact Information for Business Card

ph 0418352790
email carlwhitby@mailnest.com.au.
ABN 27813046652
name carl whitby

```html
<!DOCTYPE html>
<html lang="en">
<head>
<meta charset="utf-8">
<title>Halbrook Paving Works – Business Card</title>
<link rel="stylesheet" href="https://fonts.googleapis.com/css2?family=Quicksand:wght@500;600;700&display=swap">
<style>
  :root {
    --page-bg: #d8d5d1;
    --card-light: #e9e9e7;
    --card-light-2: #f3f3f1;
    --red-top: #ec5a36;
    --red-bottom: #c9240f;
    --brand-red: #d23a1c;
    --ink-dark: #2e2e2e;
    --text-on-red: #ffffff;
    --text-on-red-soft: rgba(255,255,255,0.88);
  }
  * { margin: 0; padding: 0; box-sizing: border-box; }
  html, body {
    width: 1200px; height: 969px; overflow: hidden;
    background: var(--page-bg);
    font-family: "Quicksand", sans-serif;
  }
  .card {
    position: absolute; left: 50px; top: 170px;
    width: 1100px; height: 628px;
    background: var(--card-light);
    overflow: hidden;
    box-shadow: 0 18px 40px rgba(0,0,0,0.18);
  }
  .card-shapes { position: absolute; inset: 0; }
  .owner { position: absolute; left: 53px; top: 66px; color: var(--text-on-red); }
  .owner-name { font-size: 39px; font-weight: 700; letter-spacing: 0.5px; text-transform: uppercase; line-height: 1.1; }
  .owner-detail { font-size: 25px; font-weight: 500; color: var(--text-on-red-soft); line-height: 38px; }
  .owner-detail:first-of-type { margin-top: 6px; }
  .services {
    position: absolute; left: 53px; top: 392px;
    list-style: none; color: var(--text-on-red-soft);
    font-size: 26px; font-weight: 500; line-height: 33px;
  }
  .services li::before {
    content: ""; display: inline-block; width: 9px; height: 9px;
    background: var(--text-on-red-soft); transform: rotate(45deg);
    margin: 0 16px 4px 4px; vertical-align: middle;
  }
  .brand-mark {
    position: absolute; left: 520px; top: 272px;
    width: 78px; height: 78px; background: var(--brand-red);
  }
  .brand-divider {
    position: absolute; left: 636px; top: 236px;
    width: 3px; height: 152px; background: var(--brand-red);
  }
  .brand-block { position: absolute; left: 662px; top: 262px; width: 400px; text-align: center; }
  .brand-name {
    font-size: 31px; font-weight: 700; color: var(--brand-red);
    text-transform: uppercase; letter-spacing: 0.5px; line-height: 1.05;
  }
  .brand-name .ruled { display: flex; align-items: center; gap: 14px; letter-spacing: 4px; }
  .brand-name .ruled::before, .brand-name .ruled::after {
    content: ""; flex: 1; height: 3px; background: var(--ink-dark);
  }
  .brand-phone { font-size: 26px; font-weight: 700; color: var(--brand-red); letter-spacing: 2px; margin-top: 2px; }
</style>
</head>
<body>
  <div class="card">
    <svg class="card-shapes" width="1100" height="628" viewBox="0 0 1100 628" aria-hidden="true">
      <defs>
        <linearGradient id="redPanel" x1="0" y1="0" x2="0.4" y2="1">
          <stop offset="0" stop-color="var(--red-top)"/>
          <stop offset="1" stop-color="var(--red-bottom)"/>
        </linearGradient>
      </defs>
      <polygon points="718,0 1100,0 1100,300 900,0" fill="var(--card-light-2)" opacity="0.8"/>
      <polygon points="718,0 412,312 718,628 1024,312" fill="var(--card-light-2)" opacity="0.55"/>
      <polygon points="0,0 718,0 412,312 718,628 0,628" fill="url(#redPanel)"/>
    </svg>

    <div class="owner">
      <p class="owner-name">Carl Whitby</p>
      <p class="owner-detail">carlwhitby@mailnest.com.au</p>
      <p class="owner-detail">ABN 27813046652</p>
    </div>

    <ul class="services">
      <li>Excavation</li>
      <li>Exposed &amp; colour concrete</li>
      <li>House &amp; shed slabs</li>
      <li>Driveways</li>
      <li>Landing &amp; steps</li>
    </ul>

    <div class="brand-mark"></div>
    <div class="brand-divider"></div>
    <div class="brand-block">
      <p class="brand-name">Halbrook Paving<span class="ruled">Works</span></p>
      <p class="brand-phone">0418352790</p>
    </div>
  </div>
</body>
</html>
```